Need posters that inspire entrepreneurs

I want to create beautiful, inspiring wall art. I'm looking for a designer to create an awesome sample (note this sample is not for real use). The winning design will form the foundation of our art "style" so there will be LOTS of ongoing work for the winning designer.

It's your challenge to create a style that is clean, inspiring and timeless, and possibly can be adapted to different colour palettes.

Looking for a perfect execution of words, image and design.

The attached example shows one idea. It should serve as an idea only.

Format of the images should be either rectangular or square. Exact size is preferably UK A4 (US letter) or max A3. Assume that a display would consist of a 4 x 4 image grid so size needs to allow for that in a small to medium size office.

The quotes I want in the 3 samples (each in an individual poster - not combined in 1 poster). Each quote should have it's own, the reason for three is to prove the design work on more than one quote. The quotes are:

1) Failure is the condiment that gives success its flavor.
– Dorian Welsby

2) Whether you think you can or think you can’t, you’re right.
– Oswald Pike

3) Ever tried. Ever failed. No matter. Try Again. Fail again. Fail better.
– Lionel Marwick

Each design should include the image of the person and the quote + any design elements you consider relevant. You should find relevant images of the individuals being quoted. The final images will not be published or used commercially in any way.

Font styles to use
Serif
Sans Serif

Colors

Designer to choose colors to be used in the design.

Requirements
Must have
• Words and headshot image - 1 per poster design.
• Please consider in the design that there will not always be photographs of the person quoted and as such the design will need to hold, whether the source is a photo, sketch or something else.
Nice to have
• None, but note that the final image will be printed on a wall mounted board, printed to the edge but not on the edge. The board will have black or white edges so consider in the design.
Should not have
• None

```html
<!DOCTYPE html>
<html lang="en">
<head>
<meta charset="utf-8">
<title>Quote Poster Series</title>
<link href="https://fonts.googleapis.com/css2?family=Libre+Baskerville:wght@400;700&family=Montserrat:wght@300;400;800&display=swap" rel="stylesheet">
<style>
  :root {
    --page: #f3f3f3;
    --ink: #ffffff;
    --ink-soft: #d4d4d4;
    --ink-muted: #8a8a8a;
    --ink-dark: #111111;
    --poster-black: #050505;
    --ghost: rgba(255,255,255,0.06);
  }
  * { margin: 0; padding: 0; box-sizing: border-box; }
  html, body { width: 1200px; height: 960px; overflow: hidden; background: var(--page); }
  .series { position: relative; width: 1200px; height: 960px; }

  .poster {
    position: absolute;
    overflow: hidden;
    background: var(--poster-black);
    box-shadow: 3px 4px 8px rgba(0,0,0,0.35);
  }
  .poster--feature { left: 305px; top: 83px; width: 590px; height: 416px; }
  .poster--left { left: 118px; top: 561px; width: 449px; height: 317px; }
  .poster--right { left: 635px; top: 561px; width: 449px; height: 317px; }

  .photo { position: absolute; }

  /* Feature poster */
  .poster--feature .photo {
    left: 330px; top: 0; width: 260px; height: 100%;
    background:
      radial-gradient(ellipse 42% 30% at 52% 38%, #c9c9c9 0%, #8f8f8f 45%, rgba(60,60,60,0) 100%),
      radial-gradient(ellipse 60% 26% at 55% 16%, #9c9c9c 0%, rgba(70,70,70,0) 100%),
      linear-gradient(180deg, rgba(5,5,5,0) 55%, #2a2a2a 70%, #1a1a1a 100%),
      linear-gradient(90deg, var(--poster-black) 0%, #1c1c1c 25%, #262626 70%, #111 100%);
  }
  .ghost-text {
    position: absolute;
    font-family: "Libre Baskerville", serif;
    font-weight: 700;
    color: var(--ghost);
    font-size: 48px;
    line-height: 40px;
    white-space: nowrap;
    transform-origin: left top;
    transform: rotate(90deg);
  }
  .ghost-text--left { left: 195px; top: 30px; }
  .ghost-text--right { left: 592px; top: 215px; }
  .verse {
    position: absolute; left: 73px; top: 112px;
    font-family: "Libre Baskerville", serif;
    font-size: 19px; line-height: 21px;
    letter-spacing: 4.5px;
    color: var(--ink);
  }
  .verse p + p { margin-top: 41px; }
  .verse b { font-weight: 700; }
  .byline {
    position: absolute; left: 109px; top: 318px; width: 140px;
    text-align: center;
    font-family: "Libre Baskerville", serif;
    color: var(--ink-soft);
  }
  .signature {
    height: 14px; width: 70px; margin: 0 auto 4px;
    background: linear-gradient(90deg, rgba(255,255,255,0) 0%, rgba(255,255,255,0.15) 50%, rgba(255,255,255,0) 100%);
  }
  .byline__rule { height: 1px; background: var(--ink-muted); margin-bottom: 5px; }
  .byline__name { font-size: 6.5px; letter-spacing: 0.6px; text-transform: uppercase; }
  .byline__dates { font-size: 5.5px; color: var(--ink-muted); margin-top: 2px; }

  /* Left poster */
  .poster--left .photo {
    inset: 0;
    background:
      radial-gradient(ellipse 22% 45% at 78% 58%, #3a3a3a 0%, #1e1e1e 55%, rgba(20,20,20,0) 100%),
      linear-gradient(180deg, rgba(0,0,0,0) 70%, #6a6a6a 85%, #9a9a9a 100%),
      radial-gradient(ellipse 75% 65% at 5% 0%, #eeeeee 0%, #a8a8a8 30%, #4a4a4a 60%, #141414 100%);
  }
  .glow {
    position: absolute; left: -30px; top: 40px; width: 370px; height: 145px;
    background: radial-gradient(closest-side, rgba(255,255,255,0.95) 0%, rgba(255,255,255,0.7) 45%, rgba(255,255,255,0) 100%);
  }
  .brackets { position: absolute; left: 20px; top: 75px; width: 268px; height: 72px; }
  .claim {
    position: absolute; left: 20px; top: 83px; width: 268px;
    text-align: center;
    font-family: "Montserrat", sans-serif;
    color: var(--ink-dark);
  }
  .claim__lead { font-size: 12.5px; font-weight: 400; letter-spacing: 1.2px; }
  .claim__mid { font-size: 8.5px; font-weight: 300; letter-spacing: 1px; color: #444; margin-top: 1px; }
  .claim__punch { font-size: 19px; font-weight: 800; letter-spacing: 1.5px; margin-top: 1px; }
  .poster--left .attribution {
    position: absolute; left: 104px; top: 166px; width: 100px; text-align: center;
    font-family: "Montserrat", sans-serif; font-size: 5px; letter-spacing: 1.5px;
    color: var(--ink-soft); text-transform: uppercase;
  }

  /* Right poster */
  .poster--right .photo {
    inset: 0;
    background:
      radial-gradient(ellipse 28% 32% at 22% 55%, #b4b4b4 0%, #7a7a7a 50%, rgba(80,80,80,0) 100%),
      radial-gradient(ellipse 30% 22% at 72% 25%, #a0a0a0 0%, rgba(90,90,90,0) 100%),
      linear-gradient(180deg, #1a1a1a 0%, #3a3a3a 30%, #5a5a5a 60%, #2a2a2a 100%);
  }
  .poster--right .shade {
    position: absolute; right: 0; top: 0; width: 230px; height: 100%;
    background: linear-gradient(90deg, rgba(0,0,0,0) 0%, rgba(0,0,0,0.55) 45%, rgba(0,0,0,0.8) 100%);
  }
  .quote {
    position: absolute; right: 25px; top: 198px;
    text-align: right;
    font-family: "Libre Baskerville", serif;
    color: var(--ink);
  }
  .quote__mark { font-size: 28px; font-weight: 700; line-height: 22px; margin-right: 4px; }
  .quote__lead { font-size: 15.5px; margin-top: 18px; }
  .quote__tail { font-size: 8.5px; margin-top: 1px; }
  .poster--right .attribution {
    font-family: "Libre Baskerville", serif;
    font-size: 4.5px; letter-spacing: 1px; text-transform: uppercase;
    color: var(--ink-soft); margin-top: 22px;
  }
</style>
</head>
<body>
<main class="series">

  <section class="poster poster--feature">
    <div class="photo" role="img" aria-label="Black and white portrait of Lionel Marwick in suit and round glasses"></div>
    <div class="ghost-text ghost-text--left" aria-hidden="true">EVER TRIED.<br>EVER FAILED.<br>NO MATTER.</div>
    <div class="ghost-text ghost-text--right" aria-hidden="true">FAIL BETTER.</div>
    <div class="verse">
      <p>EVER <b>TRIED.</b><br><b>EVER</b> FAILED.<br>NO MATTER.</p>
      <p><b>TRY</b> AGAIN.<br>FAIL <b>AGAIN.</b><br>FAIL <b>BETTER.</b></p>
    </div>
    <div class="byline">
      <div class="signature" role="img" aria-label="Handwritten signature of Lionel Marwick"></div>
      <div class="byline__rule"></div>
      <div class="byline__name">Lionel Marwick</div>
      <div class="byline__dates">(1906-1989)</div>
    </div>
  </section>

  <section class="poster poster--left">
    <div class="photo" role="img" aria-label="Black and white photo of Oswald Pike seated at a desk, in profile"></div>
    <div class="glow"></div>
    <svg class="brackets" viewBox="0 0 268 72" aria-hidden="true">
      <g fill="none" stroke="#555" stroke-width="0.8">
        <path d="M0 6V0H6"/><path d="M262 0H268V6"/>
        <path d="M0 66V72H6"/><path d="M262 72H268V66"/>
      </g>
    </svg>
    <div class="claim">
      <div class="claim__lead">WHETHER YOU THINK YOU CAN</div>
      <div class="claim__mid">OR THINK YOU CAN’T,</div>
      <div class="claim__punch">YOU’RE RIGHT.</div>
    </div>
    <div class="attribution">— Oswald Pike</div>
  </section>

  <section class="poster poster--right">
    <div class="photo" role="img" aria-label="Black and white photo of Dorian Welsby shading his eyes with one hand"></div>
    <div class="shade"></div>
    <div class="quote">
      <div class="quote__mark">“</div>
      <div class="quote__lead">Failure is the condiment</div>
      <div class="quote__tail">that gives success its flavor.</div>
      <div class="attribution">~ Dorian Welsby</div>
    </div>
  </section>

</main>
</body>
</html>
```